New business card for a regional office of a US M&A company

We need business card for a finance company, office based in Hong Kong , our Head office is in US, our business is to Merge and acquires companies , the new office will be a regional office for the Asia Pacific region. We want to use the head office logo as attached ( but don't have to be exactly the same, can be a variation to it) as a base and then add Asia Pacific alongside the logo.
We would prefer to have be bilingual Eng + Chinese, although we don't really have Chinese company name .

Industry/Entity Type

Business

Contact Information for Business Card

Carla Beth Soren
 

VP,
APAC M&A Operations
Tovar Crest Asia Pacific Limited
 
Unit 1407, K82
27 Sai Lok Fung Road, 
Hong Kong 
 
M: +852 6481 2037
T : +852 2736 4100
F : +852 2736 4155
VOIP: 4813
 
cbsoren@tovarcrest.com

Font styles to use
Serif
Sans Serif

Colors

Designer to choose colors to be used in the design.

Requirements
Must have
• APAC Office

```html
<!DOCTYPE html>
<html lang="en">
<head>
<meta charset="utf-8">
<title>Tovar Crest Asia Pacific – Business Card</title>
<link rel="stylesheet" href="https://fonts.googleapis.com/css2?family=Cormorant+Garamond:wght@500&family=Montserrat:wght@400;600;700&display=swap">
<style>
  :root {
    --bg: #2b2d31;
    --card: #f4f5f6;
    --card-edge: #e6e8ea;
    --navy: #0f2a47;
    --cyan: #1fa3cf;
    --ink: #55595e;
    --name: #4a4d52;
    --map-a: #e9ebed;
    --map-b: #dfe2e5;
  }
  * { box-sizing: border-box; margin: 0; padding: 0; }
  html, body { width: 1200px; height: 834px; overflow: hidden; }
  body {
    background: var(--bg);
    position: relative;
    font-family: "Montserrat", Arial, sans-serif;
  }
  .card {
    position: absolute;
    width: 600px;
    height: 343px;
    background: linear-gradient(135deg, #fafbfb 0%, var(--card) 60%, var(--card-edge) 100%);
    overflow: hidden;
    box-shadow: 0 10px 30px rgba(0,0,0,.35);
  }
  .card--back { left: 60px; top: 60px; }
  .card--front { left: 540px; top: 440px; }

  .map-backdrop {
    position: absolute;
    background: radial-gradient(ellipse at center, var(--map-b) 0%, var(--map-a) 55%, rgba(233,235,237,0) 80%);
    opacity: .8;
  }
  .card--back .map-backdrop { left: 30px; top: 20px; width: 540px; height: 300px; }
  .card--front .map-backdrop { left: 40px; top: 190px; width: 520px; height: 150px; }

  .top-tab {
    position: absolute;
    left: 278px; top: 0;
    width: 124px; height: 14px;
    background: var(--navy);
    border-bottom: 4px solid var(--cyan);
  }

  .brand-block {
    position: absolute;
    width: 170px; height: 100px;
    background: var(--navy);
    border-bottom: 4px solid var(--cyan);
    display: flex;
    flex-direction: column;
    align-items: center;
    justify-content: center;
    gap: 12px;
  }
  .card--back .brand-block { right: 48px; bottom: 44px; }
  .card--front .brand-block { left: 70px; top: 96px; }
  .brand-block__mark {
    width: 22px; height: 22px;
    background: #ffffff;
  }
  .brand-block__name {
    color: var(--cyan);
    font-weight: 700;
    font-size: 17px;
    letter-spacing: .5px;
  }

  .contact {
    position: absolute;
    left: 318px; top: 44px;
    color: var(--ink);
    font-size: 11.5px;
    line-height: 1.45;
  }
  .contact__name {
    font-family: "Cormorant Garamond", Georgia, serif;
    font-weight: 500;
    font-size: 19px;
    color: var(--name);
    line-height: 1.1;
  }
  .contact__title { color: var(--cyan); font-size: 12px; margin-bottom: 12px; }
  .contact__company { color: var(--cyan); font-weight: 600; }
  .contact__address { margin-bottom: 12px; }
  .contact__lines { list-style: none; margin-left: 36px; }
  .contact__lines li { display: flex; align-items: center; gap: 8px; }
  .contact__lines svg { width: 10px; height: 10px; fill: none; stroke: var(--cyan); stroke-width: 1.4; }
  .contact__lines .no-icon { padding-left: 18px; }
</style>
</head>
<body>

<section class="card card--back" aria-label="Card back">
  <div class="map-backdrop" role="img" aria-label="Faint dotted world map backdrop"></div>
  <div class="top-tab"></div>
  <div class="brand-block">
    <span class="brand-block__mark"></span>
    <span class="brand-block__name">TOVAR CREST</span>
  </div>
</section>

<section class="card card--front" aria-label="Card front">
  <div class="map-backdrop" role="img" aria-label="Faint dotted world map backdrop"></div>
  <div class="brand-block">
    <span class="brand-block__mark"></span>
    <span class="brand-block__name">TOVAR CREST</span>
  </div>
  <div class="contact">
    <p class="contact__name">Carla Beth Soren</p>
    <p class="contact__title">VP, APAC M&amp;A Operations</p>
    <p class="contact__company">Tovar Crest Asia Pacific Limited</p>
    <p class="contact__address">Unit 1407, K82<br>27 Sai Lok Fung Road,<br>Hong Kong</p>
    <ul class="contact__lines">
      <li>
        <svg viewBox="0 0 10 10" aria-hidden="true"><rect x="2.5" y="0.8" width="5" height="8.4" rx="1"/></svg>
        +852 6481 2037
      </li>
      <li>
        <svg viewBox="0 0 10 10" aria-hidden="true"><path d="M2 1 L4 1 L4.6 3 L3.4 4 Q4.5 6 6 6.6 L7 5.4 L9 6 L9 8 Q5 9 2 5 Q1 3 2 1 Z"/></svg>
        +852 2736 4100
      </li>
      <li>
        <svg viewBox="0 0 10 10" aria-hidden="true"><rect x="1" y="4" width="8" height="4.5" rx="0.8"/><rect x="3" y="1" width="4" height="3"/></svg>
        +852 2736 4155
      </li>
      <li class="no-icon">VOIP 4813</li>
    </ul>
  </div>
</section>

</body>
</html>
```